Mental Health Counselor needs advertisement design for Men's and Woman's chorus programs

I need a 1/6th page advertisement for my mental health practice named 'Quillfern Mental Health' I primarily serve the LGBTQ community, providing individual and couples/family therapy. The ad should include a 'call to action' such as Call me I can help, or Schedule an appointment today. The final design should convey familiarity with the needs of the queer community and my unique ability to help the reader with emotional concerns or relationship issues.

I would like to see designs using my logo (attached 2015-Logo.eps) and the colors of my website http://www.quillfernmentalhealth.example particularly the banner imagery (attached indigo banner.jpg and indigoMH2015.ase, bannersource.jpg)

The ad must contain the following:
Quillfern Mental Health or Quillfern Mental Health Counseling
the website address www.quillfernmentalhealth.example
phone number 206-555-0147
and my name/title: Dorian K. Whitlow Jr. MA, LMHCA/LMFTA

I am attaching the guidelines for the ad and a pdf sample of their program,

Target Market(s)

Gay, Bisexual and Transgender clients with reasonable affluence, in their late 30's- late 50's

Industry/Entity Type

Mental Health

Font styles to use
Sans Serif
Other font styles liked:
• Clerica Medium, Open Sans Family

Colors
b7a5cd
d7cce4
0455a3
ffffff

Requirements
Must have
• Must use my Logo (2015-Logo.eps attached)
Should not have
• Biased or negative language.

```html
<!DOCTYPE html>
<html lang="en">
<head>
<meta charset="utf-8">
<title>Quillfern Mental Health – I can help.</title>
<link href="https://fonts.googleapis.com/css2?family=Open+Sans:wght@300;400;700&display=swap" rel="stylesheet">
<style>
  :root {
    --page: #f2f1f4;
    --ad-bg: #e3dcee;
    --ink: #3b3a8f;
    --ink-soft: #4a4896;
    --tab: #3d358f;
    --white: #ffffff;
    --photo-light: #dcd6ea;
    --photo-mid: #b7a5cd;
    --photo-deep: #8a7fb3;
  }
  * { box-sizing: border-box; margin: 0; padding: 0; }
  html, body {
    width: 1200px; height: 1000px; overflow: hidden;
    background: var(--page);
    font-family: "Open Sans", Arial, sans-serif;
  }
  .ad {
    position: absolute; left: 100px; top: 220px;
    width: 1000px; height: 560px;
    background: var(--ad-bg);
    overflow: hidden;
  }
  .ad__headline {
    position: absolute; left: 70px; top: 40px;
    font-weight: 300; font-size: 136px; line-height: 1;
    color: var(--ink); letter-spacing: 1px;
    white-space: nowrap;
  }
  .ad__contact {
    position: absolute; left: 104px; top: 222px;
    color: var(--ink-soft);
    font-size: 20px; line-height: 1.3;
    padding-bottom: 10px;
    border-bottom: 2px solid var(--ink);
    white-space: nowrap;
    z-index: 2;
  }
  .ad__contact strong { font-weight: 700; color: var(--ink); }
  .ad__photo {
    position: absolute; right: 0; bottom: 0;
    width: 470px; height: 330px;
    background: radial-gradient(ellipse at 55% 55%, var(--photo-deep) 0%, var(--photo-mid) 30%, var(--photo-light) 65%, var(--ad-bg) 100%);
  }
  .ad__tab {
    position: absolute; left: 0; bottom: 0;
    width: 400px; height: 130px;
    background: var(--tab);
    border-top-right-radius: 22px;
    display: flex; align-items: center; gap: 16px;
    padding-left: 36px;
  }
  .ad__tab-mark {
    width: 44px; height: 44px; border-radius: 50%;
    background: var(--white); flex: none;
  }
  .ad__tab-name {
    color: var(--white); font-size: 24px; font-weight: 400;
    line-height: 1.15; white-space: nowrap;
  }
</style>
</head>
<body>
  <section class="ad" aria-label="Quillfern Mental Health advertisement">
    <h1 class="ad__headline">I can help.</h1>
    <div class="ad__contact">
      <p>Dorian K. Whitlow Jr. MA, LMHCA/LMFTA</p>
      <p>Call us at <strong>206-555-0147</strong> or visit</p>
      <p>www.<strong>quillfernmentalhealth</strong>.example</p>
    </div>
    <div class="ad__photo" role="img" aria-label="Soft lavender-toned photograph of a seated man hugging his knees, head lowered"></div>
    <div class="ad__tab">
      <span class="ad__tab-mark"></span>
      <span class="ad__tab-name">Quillfern Mental Health</span>
    </div>
  </section>
</body>
</html>
```